Business Card Design

I would like a logo created for the top left corner of the card please. I would like a checkerboard in a dark navy with the edges fading out and one random bright orange square.
Updates

I have attached some further notes and a really rough sketch of what I am after.  Thank you. :)

Target Market(s)

Construction, mining, mechanical

Industry/Entity Type

Business

Contact Information for Business Card

KRW Fabrications Pty Ltd, Oscar Plunkett, P. 0413658207, F. 0753917260, E.oscar@krwfabrications.com.au, PO Box 87 WONGARA Q 4571, ABN 52983470611

Font styles to use
Sans Serif

Requirements
Must have
• Really Dark Navy
Really bright Orange

```html
<!DOCTYPE html>
<html lang="en">
<head>
<meta charset="utf-8">
<title>KRW Fabrications Pty Ltd – Business Card</title>
<link rel="stylesheet" href="https://fonts.googleapis.com/css2?family=Arimo:wght@400;700&display=swap">
<style>
  :root {
    --stage: #1c2330;
    --navy: #0e3a66;
    --navy-deep: #0a2f55;
    --dot-blue: #1b9bd7;
    --dot-faint: #174a7c;
    --orange: #f4c21c;
    --white: #ffffff;
    --glyph: #0e3a66;
  }
  * { box-sizing: border-box; margin: 0; padding: 0; }
  html, body {
    width: 1200px;
    height: 872px;
    overflow: hidden;
    background: var(--stage);
    font-family: "Arimo", Arial, sans-serif;
  }
  .canvas {
    position: relative;
    width: 1200px;
    height: 872px;
  }
  .card {
    position: absolute;
    left: 100px;
    top: 136px;
    width: 1000px;
    height: 600px;
    border-radius: 28px;
    background: var(--navy);
    overflow: hidden;
    color: var(--white);
  }
  .halftone-corner {
    position: absolute;
    right: 0;
    top: 0;
    width: 560px;
    height: 420px;
    background: radial-gradient(ellipse at 100% 0%, var(--dot-blue) 0%, rgba(27,155,215,0.75) 35%, rgba(27,155,215,0.25) 65%, rgba(27,155,215,0) 85%);
  }
  .halftone-faint {
    position: absolute;
    left: 0;
    top: 250px;
    width: 640px;
    height: 350px;
    background: radial-gradient(ellipse at 25% 60%, var(--dot-faint) 0%, rgba(23,74,124,0.6) 45%, rgba(23,74,124,0) 80%);
  }
  .brand {
    position: absolute;
    left: 64px;
    top: 118px;
    display: flex;
    align-items: center;
    gap: 18px;
  }
  .brand-mark {
    width: 30px;
    height: 30px;
    border-radius: 4px;
    background: var(--orange);
  }
  .brand-name {
    font-weight: 700;
    font-size: 44px;
    color: var(--white);
    letter-spacing: 0.5px;
    max-width: 480px;
    line-height: 1.1;
  }
  .person {
    position: absolute;
    left: 110px;
    top: 392px;
    text-align: center;
  }
  .person-name {
    font-weight: 700;
    font-size: 28px;
  }
  .person-role {
    font-size: 22px;
    margin-top: 6px;
  }
  .contact-list {
    position: absolute;
    left: 500px;
    top: 312px;
    list-style: none;
  }
  .contact-item {
    display: flex;
    align-items: flex-start;
    gap: 16px;
    font-size: 20px;
    letter-spacing: 0.6px;
    line-height: 1.2;
    margin-bottom: 12px;
  }
  .contact-icon {
    flex: none;
    width: 22px;
    height: 22px;
  }
  .contact-text.stacked { line-height: 1.45; margin-top: -3px; }
</style>
</head>
<body>
<main class="canvas">
  <section class="card" aria-label="Business card for KRW Fabrications Pty Ltd">
    <div class="halftone-corner" role="img" aria-label="Halftone dot pattern in bright blue fading from the top right corner"></div>
    <div class="halftone-faint" role="img" aria-label="Faint halftone dot pattern in mid navy"></div>

    <div class="brand">
      <span class="brand-mark"></span>
      <h1 class="brand-name">KRW Fabrications Pty Ltd</h1>
    </div>

    <div class="person">
      <p class="person-name">Oscar Plunkett</p>
      <p class="person-role">Director</p>
    </div>

    <ul class="contact-list">
      <li class="contact-item">
        <svg class="contact-icon" viewBox="0 0 22 22" aria-hidden="true">
          <rect width="22" height="22" rx="3" fill="var(--orange)"/>
          <path d="M7 5 L9.5 5 L10.5 8 L9 9.5 Q10.5 12.5 12.5 13 L14 11.5 L17 12.5 L17 15 Q16 17 13.5 16.5 Q7 14 5.5 8.5 Q5 6 7 5Z" fill="var(--glyph)"/>
        </svg>
        <span class="contact-text">0413658207</span>
      </li>
      <li class="contact-item">
        <svg class="contact-icon" viewBox="0 0 22 22" aria-hidden="true">
          <rect width="22" height="22" rx="3" fill="var(--orange)"/>
          <rect x="7" y="4" width="8" height="5" fill="var(--glyph)"/>
          <rect x="4" y="9" width="14" height="6" rx="1" fill="var(--glyph)"/>
          <rect x="7" y="13" width="8" height="5" fill="var(--glyph)"/>
        </svg>
        <span class="contact-text">0753917260</span>
      </li>
      <li class="contact-item">
        <svg class="contact-icon" viewBox="0 0 22 22" aria-hidden="true">
          <rect width="22" height="22" rx="3" fill="var(--orange)"/>
          <rect x="4" y="6" width="14" height="10" fill="none" stroke="var(--glyph)" stroke-width="1.6"/>
          <path d="M4 6 L11 12 L18 6" fill="none" stroke="var(--glyph)" stroke-width="1.6"/>
        </svg>
        <span class="contact-text">oscar@krwfabrications.com.au</span>
      </li>
      <li class="contact-item">
        <svg class="contact-icon" viewBox="0 0 22 22" aria-hidden="true">
          <rect width="22" height="22" rx="3" fill="var(--orange)"/>
          <circle cx="11" cy="11" r="6.5" fill="none" stroke="var(--glyph)" stroke-width="1.5"/>
          <ellipse cx="11" cy="11" rx="3" ry="6.5" fill="none" stroke="var(--glyph)" stroke-width="1.3"/>
          <line x1="4.5" y1="11" x2="17.5" y2="11" stroke="var(--glyph)" stroke-width="1.3"/>
        </svg>
        <span class="contact-text">www.krwfabrications.com.au</span>
      </li>
      <li class="contact-item">
        <svg class="contact-icon" viewBox="0 0 22 22" aria-hidden="true">
          <rect width="22" height="22" rx="3" fill="var(--orange)"/>
          <path d="M11 18 Q5.5 11.5 5.5 9 A5.5 5.5 0 0 1 16.5 9 Q16.5 11.5 11 18Z" fill="var(--glyph)"/>
          <circle cx="11" cy="9" r="2" fill="var(--orange)"/>
        </svg>
        <span class="contact-text stacked">PO Box 87 WONGARA Q 4571,<br>ABN 52983470611</span>
      </li>
    </ul>
  </section>
</main>
</body>
</html>
```